Verdell Chiropractic, achieve your health goals, get better each day one step at a time

A mobile friendly site, fresh look, easy to navigate, has interface with pw/chirply, etc. Blog posts. Uses new logo. Content and address to current site is mirvaton.com. The current site will give you scope of project for content. The logo is not the final but close. Will upload final next week.
Convey the concept that heath is a process, it does not just happen. We take steps to achieve what we want in life including health.

Target Market(s)

30 to 70 year old. Needing health care

Industry/Entity Type

Health Care

Coding

Coded - Design and coding required

Number of Pages Required

5+ page

Font styles to use
Sans Serif

Colors

Designer to choose colors to be used in the design.

Requirements
Must have
• mobile friendly, easy to navigate, PW/Chirply interface, blog, room for current content
Nice to have
• potential for commerce, statistics
Should not have
• Same old look and feel as everything else out there

```html
<!DOCTYPE html>
<html lang="en">
<head>
<meta charset="utf-8">
<title>Verdell Chiropractic</title>
<link href="https://fonts.googleapis.com/css2?family=Montserrat:wght@400;500;600;700&display=swap" rel="stylesheet">
<style>
:root{
  --blue:#2f7bbf;
  --blue-dark:#1f5fa6;
  --blue-soft:#7da6d4;
  --blue-band:#3a78bd;
  --panel:#cfdeed;
  --ink:#222;
  --muted:#666;
  --footer:#3a3a3a;
  --footer-base:#2e2e2e;
  --white:#fff;
}
*{box-sizing:border-box;margin:0;padding:0}
html,body{width:1200px;height:2647px;overflow:hidden;background:var(--white);font-family:"Montserrat",sans-serif;color:var(--ink)}
.page{position:relative;width:1200px;height:2647px}
.abs{position:absolute}
.site-header{left:0;top:0;width:1200px;height:55px;background:var(--white)}
.brand{left:162px;top:17px;display:flex;align-items:center;gap:7px;font-weight:700;font-size:15px;color:var(--blue-dark)}
.brand-mark{width:14px;height:14px;background:var(--blue-dark)}
.nav{left:466px;top:21px;display:flex;gap:20px;font-size:11px;font-weight:600;white-space:nowrap}
.nav span{position:relative}
.nav .active{color:var(--blue)}
.nav .active::after{content:"";position:absolute;left:0;right:0;top:29px;height:2px;background:var(--blue)}
.hero{left:0;top:55px;width:1200px;height:508px;background:linear-gradient(90deg,#efe7e0,#d9d6d4 40%,#e6dfd8 70%,#f1ebe4)}
.services{left:0;top:563px;width:1200px;height:261px;background:var(--blue);color:var(--white)}
.services h2{position:absolute;top:48px;width:100%;text-align:center;font-size:21px;font-weight:600}
.svc{position:absolute;top:100px;width:240px;text-align:center}
.svc svg{display:block;margin:0 auto 10px}
.svc h3{font-size:13px;font-weight:600;margin-bottom:12px}
.svc p{font-size:11px;line-height:17px;white-space:nowrap}
.arrow{position:absolute;top:144px}
.divider{left:0;top:826px;width:1200px;height:2px;background:#dfe8f2}
.intro-title{left:0;top:905px;width:1200px;text-align:center;font-size:24px;font-weight:700;color:var(--blue-dark)}
.intro-text{left:0;top:954px;width:1200px;text-align:center;font-size:11px;color:var(--muted)}
.key-title{left:162px;top:992px;font-size:16px;font-weight:600}
.acc{left:162px;width:406px;height:39px;border:1px solid #dde5ee;border-radius:20px;box-shadow:0 1px 3px rgba(0,0,0,.06);display:flex;justify-content:space-between;align-items:center;padding:0 28px;font-size:12px;font-weight:600;color:var(--blue-dark)}
.acc b{font-size:18px;font-weight:400}
.acc.open{background:var(--blue);color:var(--white);border-color:var(--blue)}
.acc-body{left:182px;top:1094px;width:392px;border-left:2px solid #e2e2e2;padding-left:14px;font-size:10.2px;line-height:17px;color:var(--muted)}
.acc-body a{color:var(--blue-dark);font-weight:600;text-decoration:none}
.more-btn{left:162px;top:1451px;width:406px;height:40px;border:2px solid var(--blue-dark);border-radius:20px;text-align:center;line-height:36px;font-size:12px;font-weight:600;color:var(--blue-dark)}
.contact{left:648px;top:999px;width:362px;height:441px;background:var(--panel);padding:30px 20px}
.contact h3{font-size:16px;font-weight:600;margin-bottom:10px}
.contact address{font-style:normal;font-size:11px;line-height:19px}
.field{position:absolute;height:39px;background:var(--white);border:1px solid #b9cde3;font-size:10px;color:#9aa;padding:0 12px;line-height:37px}
.captcha-note{position:absolute;left:188px;top:316px;font-size:9px}
.submit{position:absolute;left:22px;top:350px;width:318px;height:39px;background:var(--blue);border-radius:20px;color:var(--white);text-align:center;line-height:39px;font-size:12px;font-weight:700}
.lic-photo{left:0;top:1571px;width:1200px;height:317px;background:linear-gradient(90deg,#dfe3e6,#bfc6cc 45%,#e8e9ea 75%,#f3f3f3)}
.lic-box{left:187px;top:1650px;width:826px;height:171px;background:rgba(232,240,248,.85);text-align:center}
.lic-box h3{margin-top:28px;font-size:19px;font-weight:600}
.lic-box hr{width:490px;margin:12px auto 14px;border:0;border-top:1px dashed #333}
.lic-box p{font-size:20px;font-weight:600;line-height:28px}
.doctor{left:0;top:1888px;width:1200px;height:277px;background:var(--blue-soft)}
.doc-photo{left:185px;top:1903px;width:221px;height:262px;background:linear-gradient(180deg,#c9a98f,#3a3033 60%,#222);border-radius:110px 110px 0 0}
.doc-text{left:473px;top:1945px;width:560px;color:var(--white);font-size:16px;font-weight:600;line-height:22px}
.doc-text strong{color:#111;font-weight:600}
.doc-text hr{border:0;border-top:1px dashed var(--white);margin:18px 0 18px}
.blogs{left:0;top:2165px;width:1200px;height:279px;background:var(--blue-band);color:var(--white)}
.blogs h2{position:absolute;left:187px;top:40px;font-size:21px;font-weight:600}
.blog-photo{left:187px;top:2254px;width:242px;height:136px;background:linear-gradient(135deg,#dfe6ea,#8a9199 60%,#c7ced3);border:2px solid var(--white)}
.blog-card{left:448px;top:2254px;width:567px;height:136px;background:var(--white);padding:20px 28px;font-size:11px;line-height:18px;color:var(--muted)}
.blog-card cite{display:block;font-style:normal;color:var(--blue-dark);font-weight:600;margin-top:4px}
.quote{position:absolute;right:18px;bottom:10px;font-size:56px;color:#ddd;font-family:Georgia,serif;line-height:40px}
.footer{left:0;top:2444px;width:1200px;height:163px;background:var(--footer);color:#ddd}
.footer h4{position:absolute;font-size:13px;font-weight:500}
.f-list{position:absolute;left:162px;top:56px;font-size:11px;line-height:26px}
.f-list svg{vertical-align:middle;margin-right:8px}
.social{position:absolute;left:596px;top:63px;display:flex;gap:6px}
.social span{width:24px;height:24px;background:#8a8a8a}
.f-brand{position:absolute;left:800px;top:38px;font-size:20px;font-weight:700;color:var(--blue-soft)}
.f-tag{position:absolute;left:800px;top:92px;width:260px;font-size:11px;line-height:16px}
.base{left:0;top:2607px;width:1200px;height:40px;background:var(--footer-base);color:#bbb;font-size:10px}
.base .copy{position:absolute;left:162px;top:14px}
.base .links{position:absolute;right:162px;top:14px}
</style>
</head>
<body>
<div class="page">
  <header class="site-header abs">
    <div class="brand abs"><span class="brand-mark"></span>VERDELL CHIROPRACTIC</div>
    <nav class="nav abs">
      <span class="active">Home</span><span>Meet Dr.Hallorin</span><span>Services</span><span>Testimonials</span><span>FAQ's</span><span>Resources</span><span>Blog</span><span>Contact Us</span>
    </nav>
  </header>

  <div class="hero abs" role="img" aria-label="Photo of a person holding their lower back in pain"></div>

  <section class="services abs">
    <h2>Verdell Chiropractic Services</h2>
    <svg class="arrow" style="left:120px" width="12" height="16"><path d="M10 1 2 8l8 7z" fill="#fff"/></svg>
    <svg class="arrow" style="left:1068px" width="12" height="16"><path d="M2 1l8 7-8 7z" fill="#fff"/></svg>
    <div class="svc" style="left:132px"><svg width="32" height="32"><rect x="10" y="3" width="12" height="5" fill="#fff"/><rect x="10" y="11" width="12" height="5" fill="#fff"/><rect x="10" y="19" width="12" height="5" fill="#fff"/><rect x="10" y="27" width="12" height="4" fill="#fff"/></svg><h3>Chiropractic</h3><p>As a Chiropractor, Dr.Hallorin focu-<br>ses on disorders of the musc...</p></div>
    <div class="svc" style="left:367px"><svg width="32" height="32"><circle cx="16" cy="10" r="6" fill="none" stroke="#fff" stroke-width="2"/><path d="M6 30c2-8 18-8 20 0" fill="none" stroke="#fff" stroke-width="2"/></svg><h3>Acupuncture</h3><p>As a Chiropractor, Dr.Hallorin focu-<br>ses on disorders of the musc...</p></div>
    <div class="svc" style="left:600px"><svg width="32" height="32"><circle cx="16" cy="13" r="10" fill="#fff"/><rect x="12" y="22" width="8" height="8" fill="#fff"/></svg><h3>Applied Kinesiology</h3><p>As a Chiropractor, Dr.Hallorin focu-<br>ses on disorders of the musc...</p></div>
    <div class="svc" style="left:826px"><svg width="32" height="32"><circle cx="14" cy="8" r="5" fill="#fff"/><rect x="4" y="18" width="24" height="5" fill="#fff"/><rect x="6" y="25" width="3" height="6" fill="#fff"/><rect x="23" y="25" width="3" height="6" fill="#fff"/></svg><h3>Massage</h3><p>As a Chiropractor, Dr.Hallorin focu-<br>ses on disorders of the musc...</p></div>
  </section>
  <div class="divider abs"></div>

  <h2 class="intro-title abs">Verdell Chiropractic</h2>
  <p class="intro-text abs">Dr. Hallorin's practice has been centered around the use of Applied Kinesiology (AK) for over 25 years.&nbsp; AK is a technique used to evaluate structural.</p>

  <h3 class="key-title abs">Our Key Services</h3>
  <div class="acc open abs" style="top:1040px">Headaches<b>−</b></div>
  <p class="acc-body abs">Chronic headaches and migraines afflict many Americans.&nbsp; The often debilitating pain affects their families and jobs.&nbsp; The primary causes are structural (spinal nerves and muscles), chemical <a>..Read More</a></p>
  <div class="acc abs" style="top:1167px">Neck Pain<b>+</b></div>
  <div class="acc abs" style="top:1214px">Shoulder Pain<b>+</b></div>
  <div class="acc abs" style="top:1262px">Wrist Pain<b>+</b></div>
  <div class="acc abs" style="top:1309px">Lower Back Pain<b>+</b></div>
  <div class="acc abs" style="top:1356px">Hip &amp; Leg Pain<b>+</b></div>
  <div class="acc abs" style="top:1403px">Knee Pain<b>+</b></div>
  <div class="more-btn abs">Read More Services</div>

  <aside class="contact abs">
    <h3>Contact Us</h3>
    <address>4870 Prairie Gate Road<br>Harlow, TX&nbsp; 75021<br>555.201.4480 Off</address>
    <div class="field" style="left:20px;top:131px;width:158px">First Name</div>
    <div class="field" style="left:184px;top:131px;width:158px">Last Name</div>
    <div class="field" style="left:20px;top:177px;width:322px">Email</div>
    <div class="field" style="left:20px;top:224px;width:322px">Company</div>
    <div class="field" style="left:20px;top:271px;width:158px">Phone Number</div>
    <div class="field" style="left:184px;top:271px;width:158px;color:#333;font-size:16px;font-weight:600">7002</div>
    <span class="captcha-note">Type the text in the field</span>
    <div class="submit">SUBMIT</div>
  </aside>

  <div class="lic-photo abs" role="img" aria-label="Photo of a chiropractor adjusting a patient's neck"></div>
  <div class="lic-box abs">
    <h3>Licensure</h3>
    <hr>
    <p>Lone Mesa Board of Chiropractic Examiners<br>High Plains Board of Chiropractic Examiners</p>
  </div>

  <section class="doctor abs"></section>
  <div class="doc-photo abs" role="img" aria-label="Portrait of the doctor with his wife"></div>
  <div class="doc-text abs">
    <strong>DR. CALDEN HALLORIN WITH WIFE MARISOL :</strong> Caprock Chiropractic College 1991, Doctor of Chiropractic with honors
    <hr>
    Additional Education : Diplomate, Allied Board of Homeopatic Examiners, 1991, Diplomate, Regional Council of Clinical Nutritionist, 1996, Certified, Clinical Nutritionist, Northland Academy of...
  </div>

  <section class="blogs abs">
    <h2>Verdell Chiropractic Blogs</h2>
    <svg class="arrow" style="left:120px;top:142px" width="12" height="16"><path d="M10 1 2 8l8 7z" fill="#fff"/></svg>
    <svg class="arrow" style="left:1068px;top:142px" width="12" height="16"><path d="M2 1l8 7-8 7z" fill="#fff"/></svg>
  </section>
  <div class="blog-photo abs" role="img" aria-label="Photo of a man at a desk holding his sore back"></div>
  <div class="blog-card abs">
    I am an M.D., and advised many of my patients to consult with Dr. Hallorin.&nbsp; Those who took my advice got better quickly.&nbsp; I, personally, have used Dr. Hallorin's services on numerous occasions, have always found relief for my conditions, and have saved hundreds of dollars, which otherwise would have been spent on medications...
    <cite>TMR, M.D., Harlow TX</cite>
    <span class="quote">”</span>
  </div>

  <footer class="footer abs">
    <h4 style="left:162px;top:26px">Contact us</h4>
    <div class="f-list">
      <div><svg width="9" height="12"><path d="M4.5 0A4.5 4.5 0 0 0 0 4.5C0 8 4.5 12 4.5 12S9 8 9 4.5A4.5 4.5 0 0 0 4.5 0z" fill="#999"/></svg>Address: 4870 Prairie Gate Road, Harlow, TX&nbsp; 75021</div>
      <div><svg width="11" height="11"><path d="M2 0l3 3-1.5 2a7 7 0 0 0 3 3L8 6.5l3 3L9.5 11C4 11 0 7 0 1.5z" fill="#999"/></svg>Phone: 1555.201.4480&nbsp; / &nbsp;Fax : 555.201.4490</div>
      <div><svg width="12" height="9"><rect width="12" height="9" fill="#999"/><path d="M0 0l6 5 6-5" fill="none" stroke="#3a3a3a"/></svg>E-mail: info@mirvaton.com</div>
    </div>
    <h4 style="left:596px;top:26px">Follow us</h4>
    <div class="social"><span></span><span></span><span></span></div>
    <div class="f-brand">VERDELL CHIROPRACTIC</div>
    <p class="f-tag">Caprock Chiropractic College 1991, Doctor of Chiropractic with honors</p>
  </footer>
  <div class="base abs">
    <span class="copy">©2018 Verdell Chiropractic Allrights are Reserved.</span>
    <span class="links">Terms &amp; Condition&nbsp; |&nbsp; Privacy policy</span>
  </div>
</div>
</body>
</html>
```